Psychology service brochure

Marketing brochure for a new psychological counselling service.
Our old brochure was too boring and conservative. We are selling our services to GP's, psychiatrists, other health providers and of course potential clients. We'd really like a professional, elegant look that conveys us to be compassionate and conscientious providers of psychological services.
I have included a copy of our old brochure and a copy of the changes we'd like to the text.
Updates
I have included a photo of myself and my business partner. Only the faces are needed, so backgrounds would need to be edited out.
Hello, in consultation with my business partner, we would like
the use of our photos in the brochure please (with backgrounds edited out)
no stock photos of random people
use of abstract or nature/floral motifs suggestive of tranquillity
regards,
Miriam
Target Market(s)
General practitioner doctors, potential clients
Industry/Entity Type
Health
Requirements
Must have
- must include BlairMdITC TT- font for the business name
- must include our signature color Pantone 291 (see attached brochure)
- use of the photos of myself and my business partner (with background edited out please)
- keep use of colours to a minimum, 3 colors maximum, one of which must be Pantone 291
- must include changes to the brochure as outlined in the 'Changes to Pamphlet' document.
Nice to have
- an interesting, eye catching layout.
- interesting use of white spaces
- use of subtle abstract or nature/floral related graphics suggestive of tranquillity
Should not have
- should not include our fee
- stock photos of people

```html
<!DOCTYPE html>
<html lang="en">
<head>
<meta charset="utf-8">
<title>Stillwater Counselling — Brochure</title>
<link href="https://fonts.googleapis.com/css2?family=Open+Sans:ital,wght@0,400;0,600;1,400&family=Arimo:ital,wght@0,400;1,700&family=Questrial&family=Berkshire+Swash&display=swap" rel="stylesheet">
<style>
  :root {
    --sky: #3aa8e0;
    --sky-deep: #1f8fd0;
    --band: #a3d2f0;
    --ring: #a5e3f8;
    --white: #ffffff;
  }
  * { margin: 0; padding: 0; box-sizing: border-box; }
  html, body { width: 1200px; height: 840px; overflow: hidden; background: var(--white); }
  .brochure { position: relative; width: 1200px; height: 840px; overflow: hidden; background: var(--white); font-family: "Arimo", sans-serif; }

  /* Left panel */
  .floral-wash { position: absolute; left: 0; top: 0; width: 400px; height: 805px;
    background: radial-gradient(ellipse at 20% 35%, #e4edf6 0%, rgba(238,244,250,0.6) 45%, rgba(255,255,255,0) 75%); }
  .section-band { position: absolute; left: 0; width: 400px; background: var(--band); color: var(--white);
    font-style: italic; font-weight: 700; font-size: 23px; line-height: 30px; padding-left: 40px; }
  .section-band.approach { top: 59px; height: 34px; line-height: 34px; }
  .section-band.goals { top: 452px; height: 69px; padding-top: 4px; }
  .panel-text { position: absolute; left: 49px; width: 340px; color: var(--sky); font-size: 15.3px; line-height: 19.6px; }
  .panel-text p + p { margin-top: 19.6px; }
  .approach-text { top: 120px; }
  .goal-list { position: absolute; left: 34px; top: 542px; width: 360px; list-style: none; color: var(--sky); font-size: 15.3px; line-height: 19.8px; }
  .goal-list li { padding-left: 13px; text-indent: -13px; }
  .goal-list li::before { content: "* "; }

  /* Footer band */
  .footer-band { position: absolute; left: 0; bottom: 0; width: 801px; height: 35px; background: var(--band); }
  .footer-band span { position: absolute; top: 9px; font-family: "Questrial", sans-serif; color: var(--white); font-size: 15px; letter-spacing: 2.2px; }
  .footer-band span.first { left: 12px; }
  .footer-band span.second { left: 414px; }

  /* Middle panel */
  .top-bar { position: absolute; left: 401px; top: 0; width: 400px; height: 33px; background: var(--band); }
  .location-map { position: absolute; left: 428px; top: 117px; width: 345px; height: 293px;
    background: linear-gradient(180deg, #e8f4fc 0%, #d6ecfa 100%); }
  .ornament { position: absolute; left: 521px; top: 492px; width: 153px; height: 94px;
    background: radial-gradient(ellipse at center, #d7dce2 0%, #eceff2 60%, rgba(255,255,255,0) 100%); }
  .contact-title { position: absolute; left: 401px; top: 598px; width: 400px; text-align: center;
    font-family: "Berkshire Swash", cursive; font-weight: 400; color: var(--sky); font-size: 33px; letter-spacing: 1px; }
  .contact-details { position: absolute; left: 401px; top: 664px; width: 400px; text-align: center; font-style: normal;
    font-family: "Open Sans", sans-serif; color: #4aa3d6; font-size: 17px; line-height: 21.5px; }
  .contact-details strong { font-weight: 600; }

  /* Cover panel */
  .cover { position: absolute; left: 801px; top: 0; width: 399px; height: 805px; }
  .cover-wave { position: absolute; left: 0; top: 0; width: 399px; height: 805px;
    background: linear-gradient(200deg, #3cc3f2 0%, #2ea3de 38%, #7fcdf2 55%, #d6eefb 65%, #ffffff 75%); }
  .cover-ring { position: absolute; left: 0; top: 0; }
  .cover-title { position: absolute; left: 0; top: 146px; width: 399px; text-align: center; color: var(--white);
    font-family: "Questrial", sans-serif; font-weight: 400; font-size: 23px; letter-spacing: 3px; line-height: 28px; }
  .cover-rule { position: absolute; left: 0; width: 399px; height: 0; border-top: 2px dashed rgba(255,255,255,0.45); }
  .cover-rule.upper { top: 124px; }
  .cover-rule.lower { top: 213px; }
  .medicare-note { position: absolute; left: 826px; top: 792px; width: 240px; color: var(--sky-deep);
    font-family: "Open Sans", sans-serif; font-style: italic; font-size: 12px; line-height: 16px; }
</style>
</head>
<body>
<main class="brochure">

  <section class="panel-inside">
    <div class="floral-wash" role="img" aria-label="Soft pale floral leaf pattern in the background"></div>

    <h2 class="section-band approach">Our Approach to Therapy</h2>
    <div class="panel-text approach-text">
      <p>We are warm, compassionate and<br>professional Clinical and General<br>Psychologists who together have<br>thirty years of experience and<br>who are committed to providing<br>high quality evidence-based treatment<br>to our clients.</p>
      <p>Types of treatment may include<br>Cognitive Behavioural Therapy,<br>Interpersonal Psychotherapy,<br>Motivational Interviewing and<br>Mindfulness.</p>
    </div>

    <h2 class="section-band goals">What We Want for<br>Our Client</h2>
    <ul class="goal-list">
      <li>for you to feel heard and respected</li>
      <li>to have a positive experience of<br>working collaboratively with a psychologist</li>
      <li>to correct or reconnect with feelings of hope</li>
      <li>to move beyond counselling with<br>an understanding of your own strengths<br>and the skills to make changes that will<br>help you meet future challenges.</li>
    </ul>
  </section>

  <section class="panel-contact">
    <div class="top-bar"></div>
    <div class="location-map" role="img" aria-label="Street map showing the centre location near the train station"></div>
    <div class="ornament" role="img" aria-label="Grey decorative scroll ornament"></div>
    <h2 class="contact-title">Contact Reception</h2>
    <address class="contact-details">
      The Kestrel Centre<br>
      18 Kestrel Street<br>
      Phone : <strong>9350 2714 9350 6082</strong><br>
      Email : hello@stillwatercounsel.com
    </address>
  </section>

  <footer class="footer-band">
    <span class="first">STILLWATER COUNSELLING</span>
    <span class="second">STILLWATER COUNSELLING</span>
  </footer>

  <section class="cover">
    <div class="cover-wave" role="img" aria-label="Abstract blue wave pattern sweeping across the cover"></div>
    <svg class="cover-ring" width="399" height="805" viewBox="0 0 399 805" aria-hidden="true">
      <circle cx="405" cy="830" r="75" fill="none" stroke="var(--ring)" stroke-width="28"/>
    </svg>
    <div class="cover-rule upper"></div>
    <h1 class="cover-title">STILLWATER<br>COUNSELLING</h1>
    <div class="cover-rule lower"></div>
  </section>

  <p class="medicare-note">* eligible to provide Pregnancy Support<br>&nbsp;&nbsp;Counselling services under Medicare</p>

</main>
</body>
</html>
```